Fundraiser Flyer and Email Template

We are looking for a flexible coordinated flyer and email template. The feel of both should be more formal or professional. We are not looking for an overly "political" design that features American flags or other "political" symbols.

We are a political fundraising firm that works with elected officials to set up fundraisers for their campaigns. We send the invites to these events via US Mail and email, so we are looking for a standardized template that will work as both an 8.5 x 11 inch printed flyer, as well as an email template.

The information in the email will be text, but images can be used for formatting.

Some clients have a campaign logo, others do not. The format should be flexible enough to either include the logo, or leave it out. Size also varies.

Any colors in the template should be editable so we can match logos as we get them.

We're open to any format that allows us to edit the format as needed. This would include Photoshop, Microsoft Word, etc.

The text of the invite should include space for:

---------------------------------------
NAME
DISTRICT NUMBER AND OFFICE

DATE OF EVENT
TIME OF EVENT

LOCATION
LOCATION ADDRESS
LOCATION CITY, STATE, ZIP

SUGGESTED CONTRIBUTION LEVELS (Typically 3 levels are provided such as Gold: $1,000, Silver: $500, Bronze: $250)

ADDRESS TO SEND CHECKS TO

RSVP CONTACT INFORMATION

The invite will also need fine-print at the bottom that reads:
"Pennsylvania law allows personal, partnership, and PAC contributions. By law we cannot accept corporate contributions
Paid for by [NAME]"

Industry/Entity Type

It Professional

Font styles to use
Serif
Sans Serif

Requirements
Must have
• Must have spaces for:
• NAME
• DISTRICT NUMBER AND OFFICE
• DATE OF EVENT
• TIME OF EVENT
• LOCATION
• LOCATION ADDRESS
• LOCATION CITY, STATE, ZIP
• SUGGESTED CONTRIBUTION LEVELS (Typically 3 levels are provided such as Gold: $1,000, Silver: $500, Bronze: $250)
• ADDRESS TO SEND CHECKS TO
• RSVP CONTACT INFORMATION
• The invite will also need fine-print at the bottom that reads:
• "Pennsylvania law allows personal, partnership, and PAC contributions. By law we cannot accept corporate contributions
• Paid for by [NAME]"
Should not have
• It should not be overly "political".

```html
<!DOCTYPE html>
<html lang="en">
<head>
<meta charset="utf-8">
<title>Fundraiser Invitation Flyer</title>
<link rel="stylesheet" href="https://fonts.googleapis.com/css2?family=Oswald:wght@500;600&family=Lato:wght@300;400;700;900&display=swap">
<style>
  :root {
    --accent: #22c4ef;
    --ink-dark: #2e3336;
    --ink-dark-2: #3a3f43;
    --paper: #ffffff;
    --panel-light: #f3f3f3;
    --label: #2b2b2b;
    --backdrop: #ececec;
  }
  * { box-sizing: border-box; margin: 0; padding: 0; }
  html, body { width: 1200px; height: 1200px; overflow: hidden; }
  body {
    background: var(--backdrop);
    font-family: "Lato", Arial, sans-serif;
    position: relative;
  }
  .flyer {
    position: absolute;
    left: 151px; top: 20px;
    width: 897px; height: 1160px;
    background: var(--paper);
    overflow: hidden;
  }
  .hero-photo {
    position: absolute; left: 0; top: 0; width: 897px; height: 560px;
    background:
      linear-gradient(180deg, rgba(255,255,255,0) 0%, rgba(255,255,255,0) 55%, rgba(255,255,255,0.85) 88%, #fff 100%),
      radial-gradient(ellipse at 30% 35%, #d9b29a 0%, rgba(217,178,154,0) 35%),
      radial-gradient(ellipse at 70% 40%, #c99a7c 0%, rgba(201,154,124,0) 30%),
      radial-gradient(ellipse at 85% 70%, #7e9a3c 0%, rgba(126,154,60,0) 28%),
      linear-gradient(90deg, #3c4146 0%, #e9ecee 30%, #f4f2f0 55%, #4a4e52 80%, #cfe2e0 100%);
  }
  .headline {
    position: absolute; left: 0; width: 100%; text-align: center;
  }
  .headline-district {
    top: 318px;
    font-family: "Oswald", "Arial Narrow", sans-serif;
    font-weight: 600; font-size: 96px; line-height: 1;
    color: #fff; letter-spacing: -1px;
    transform: scaleX(0.82);
    text-shadow: 0 2px 6px rgba(0,0,0,0.25);
  }
  .headline-office {
    top: 396px;
    font-family: "Lato", Arial, sans-serif;
    font-weight: 700; font-size: 92px; line-height: 1;
    color: var(--accent); letter-spacing: -1px;
  }
  .headline-reflection {
    top: 484px;
    font-weight: 700; font-size: 92px; line-height: 1;
    color: var(--accent); letter-spacing: -1px;
    transform: scaleY(-1);
    opacity: 0.18;
    -webkit-mask-image: linear-gradient(0deg, #000 0%, transparent 55%);
    mask-image: linear-gradient(0deg, #000 0%, transparent 55%);
  }
  .details-band {
    position: absolute; left: 0; top: 544px; width: 100%; height: 234px;
    background: linear-gradient(180deg, var(--ink-dark-2), var(--ink-dark));
    color: #fff; text-align: center;
  }
  .ribbon {
    position: absolute; left: 181px; top: 531px; width: 536px; height: 58px;
    background: var(--accent);
    display: flex; align-items: center; justify-content: center;
  }
  .ribbon-fold { position: absolute; top: 531px; }
  .ribbon-title {
    font-family: "Oswald", "Arial Narrow", sans-serif;
    font-weight: 500; font-size: 44px; color: #fff; line-height: 1;
    transform: scaleX(0.8); white-space: nowrap;
  }
  .levels {
    position: absolute; top: 596px; left: 0; width: 100%;
    text-align: center; color: #fff;
    font-weight: 400; font-size: 28px; line-height: 35px;
  }
  .checks-address {
    position: absolute; top: 676px; left: 0; width: 100%; text-align: center;
    font-weight: 900; font-size: 33px; color: var(--accent); line-height: 1;
  }
  .rsvp {
    position: absolute; top: 705px; left: 0; width: 100%; text-align: center;
    font-weight: 300; font-size: 50px; color: #fff; line-height: 1;
  }
  .event-panel {
    position: absolute; left: 0; top: 778px; width: 100%; height: 246px;
    background: linear-gradient(180deg, var(--panel-light), #fafafa 60%, #f0f0f0);
  }
  .field {
    position: absolute; font-weight: 700; font-size: 21px; color: var(--label);
    display: flex; align-items: baseline; white-space: nowrap;
  }
  .field-line {
    display: inline-block; border-bottom: 2px dotted #555; margin-left: 6px; height: 1px;
  }
  .field-date { left: 32px; top: 848px; }
  .field-time { left: 32px; top: 918px; }
  .field-location { left: 503px; top: 848px; }
  .address-line {
    position: absolute; left: 503px; width: 358px; border-bottom: 2px dotted #555;
  }
  .fine-print {
    position: absolute; left: 0; top: 1024px; width: 100%; height: 127px;
    background: var(--ink-dark); color: #fff; text-align: center;
    padding-top: 16px; font-size: 17px; line-height: 23px;
  }
  .fine-print-intro { font-weight: 700; margin-bottom: 5px; }
  .fine-print-paid { color: var(--accent); }
</style>
</head>
<body>
  <main class="flyer">
    <div class="hero-photo" role="img" aria-label="Photo of a cheering group of business professionals with raised arms"></div>

    <h1 class="headline headline-district">DISTRICT NUMBER</h1>
    <h2 class="headline headline-office">AND OFFICE</h2>
    <div class="headline headline-reflection" aria-hidden="true">AND OFFICE</div>

    <section class="details-band"></section>

    <svg class="ribbon-fold" style="left:165px" width="16" height="14" viewBox="0 0 16 14" aria-hidden="true"><polygon points="16,0 16,14 0,14" fill="#1593b5"/></svg>
    <svg class="ribbon-fold" style="left:717px" width="16" height="14" viewBox="0 0 16 14" aria-hidden="true"><polygon points="0,0 0,14 16,14" fill="#1593b5"/></svg>
    <div class="ribbon"><span class="ribbon-title">SUGGESTED CONTRIBUTION LEVELS</span></div>

    <p class="levels">(Typically 3 levels are provided such as Gold:<br>$1,000, Silver: $500, Bronze: $250)</p>
    <p class="checks-address">ADDRESS TO SEND CHECKS TO</p>
    <p class="rsvp">RSVP CONTACT INFORMATION</p>

    <section class="event-panel"></section>
    <div class="field field-date">DATE OF EVENT:<span class="field-line" style="width:212px"></span></div>
    <div class="field field-time">TIME OF EVENT:<span class="field-line" style="width:212px"></span></div>
    <div class="field field-location">LOCATION:<span class="field-line" style="width:236px"></span></div>
    <div class="address-line" style="top:923px"></div>
    <div class="address-line" style="top:976px"></div>

    <footer class="fine-print">
      <p class="fine-print-intro">The invite will also need fine-print at the bottom that reads:</p>
      <p>"Pennsylvania law allows personal, partnership, and PAC contributions. By law we cannot accept<br>corporate contributions</p>
      <p class="fine-print-paid">Paid for by [NAME]"</p>
    </footer>
  </main>
</body>
</html>
```